Organic Food Packaging for Bulk Nuts, Seeds, Dried fruit

We need a simple yet creative packaging design for our vitanest brand. The packaging will be for stand up bags. We would like a very simply design that we can use for all of our packaging needs. The size of the pouch is 6" wide by 12" tall. You can visit our site. www.vitanest.example to get some ideas. Here are some packaging ideas we do like. https://wrappers.sampleboard.example/contest/4720948https://designmart.example/item/dry-fuits-bag-packaging/27939773

Target Market(s)

organic foods, health food, green, speciality and gourmet shops

Industry/Entity Type

Food Production

Font styles to use
Sans Serif

Requirements
Must have
• We need space in the middle of the pouch to be white so we can apply labels on it.
Nice to have
• Simple vines, leaves, gray patterns, 2-3 color design will be best. We would like a see through window. I have attached our logo.
Should not have
• many colors or lots of background colors.

```html
<!DOCTYPE html>
<html lang="en">
<head>
<meta charset="utf-8">
<title>vitanest – stand-up pouch front</title>
<link href="https://fonts.googleapis.com/css2?family=Open+Sans:wght@400;600&display=swap" rel="stylesheet">
<style>
  :root {
    --stage: #e6e6e6;
    --leaf-green: #8dc14f;
    --deep-green: #79b23c;
    --gold: #c9a03a;
    --cream: #f4ecd0;
    --paper: #ffffff;
    --ink: #3d3d3d;
  }
  html, body {
    margin: 0;
    width: 1200px;
    height: 1200px;
    overflow: hidden;
    background: var(--stage);
    font-family: "Open Sans", sans-serif;
  }
  .pouch {
    position: absolute;
    left: 300px;
    top: 154px;
    width: 600px;
    height: 892px;
    background: var(--paper);
    overflow: hidden;
  }
  .pouch__border-art {
    position: absolute;
    inset: 0;
    background:
      radial-gradient(ellipse 230px 300px at 300px 430px, var(--paper) 0%, var(--paper) 55%, rgba(255,255,255,0) 100%),
      linear-gradient(90deg, #e3d49a 0%, var(--cream) 16%, #fbf7ea 40%, #fbf7ea 60%, var(--cream) 84%, #d9e6b8 100%);
  }
  .pouch__top-band {
    position: absolute;
    left: 0; top: 0;
    width: 100%;
    height: 88px;
    background: var(--leaf-green);
    display: flex;
    align-items: center;
    justify-content: center;
    gap: 14px;
  }
  .brand-mark {
    width: 26px; height: 26px;
    border-radius: 50%;
    background: var(--paper);
  }
  .brand-name {
    color: var(--paper);
    font-weight: 400;
    font-size: 44px;
    letter-spacing: 1px;
  }
  .pouch__bottom-band {
    position: absolute;
    left: 0; bottom: 0;
    width: 100%;
    height: 28px;
    background: var(--leaf-green);
  }
  .watercolor-wash {
    position: absolute;
    left: 175px; top: 262px;
    width: 250px; height: 250px;
    border-radius: 50%;
    background: radial-gradient(circle, #dfe98f 0%, #e6ee9f 45%, rgba(240,245,200,0.6) 70%, rgba(255,255,255,0) 100%);
  }
  .claim {
    position: absolute;
    left: 0;
    width: 100%;
    text-align: center;
    margin: 0;
    white-space: nowrap;
  }
  .claim--percent { top: 184px; color: var(--gold); font-size: 19px; line-height: 26px; }
  .claim--ribbon {
    top: 212px;
    left: 206px;
    width: 188px;
    box-sizing: border-box;
    border: 2px solid var(--leaf-green);
    color: var(--leaf-green);
    font-size: 22px;
    line-height: 30px;
  }
  .claim--small { top: 252px; color: var(--leaf-green); font-size: 10px; line-height: 14px; letter-spacing: .3px; }
  .emblem {
    position: absolute;
    left: 265px; top: 360px;
    width: 70px; height: 70px;
    border-radius: 50%;
    background: radial-gradient(circle, #e8c66a 0%, var(--gold) 60%, var(--leaf-green) 100%);
  }
  .label-frame {
    position: absolute;
    left: 132px; top: 414px;
  }
  .label-title {
    top: 436px;
    color: var(--gold);
    font-size: 36px;
    line-height: 48px;
    font-weight: 400;
  }
  .label-sub {
    top: 495px;
    color: var(--gold);
    font-size: 16px;
    line-height: 22px;
  }
  .badge {
    position: absolute;
    top: 736px;
    width: 76px; height: 76px;
    box-sizing: border-box;
    border: 2px solid var(--ink);
    border-radius: 50%;
    display: flex;
    flex-direction: column;
    align-items: center;
    justify-content: center;
    background: rgba(255,255,255,0.55);
    line-height: 1.05;
  }
  .badge__big { font-size: 16px; color: var(--ink); }
  .badge__small { font-size: 10px; color: var(--ink); }
  .badge__small--green { color: var(--leaf-green); }
  .badge--quality { left: 114px; }
  .badge--gmo { left: 246px; }
  .badge--fresh { left: 378px; }
</style>
</head>
<body>
  <main class="pouch">
    <div class="pouch__border-art" role="img" aria-label="Hand-drawn green and golden leaves and vines framing the pouch edges"></div>

    <header class="pouch__top-band">
      <span class="brand-mark"></span>
      <span class="brand-name">vitanest</span>
    </header>

    <div class="watercolor-wash" role="img" aria-label="Soft lime-green watercolour wash behind the label area"></div>

    <p class="claim claim--percent">100%</p>
    <p class="claim claim--ribbon">VEGAN FOOD</p>
    <p class="claim claim--small">NATURAL PRODUCT</p>

    <div class="emblem" role="img" aria-label="Gold and green leaf rosette emblem"></div>

    <svg class="label-frame" width="336" height="94" viewBox="0 0 336 94" aria-hidden="true">
      <g fill="none" stroke="#8dc14f" stroke-width="2.5">
        <polyline points="110,2 1.25,2 1.25,92 60,92"/>
        <polyline points="226,2 334.75,2 334.75,92 276,92"/>
      </g>
    </svg>
    <p class="claim label-title">Flavour or Label</p>
    <p class="claim label-sub">NATURAL PRODUCT</p>

    <div class="badge badge--quality">
      <span class="badge__big">100%</span>
      <span class="badge__small">QUALITY</span>
    </div>
    <div class="badge badge--gmo">
      <span class="badge__big">GMO</span>
      <span class="badge__small badge__small--green">FREE</span>
    </div>
    <div class="badge badge--fresh">
      <span class="badge__big">100%</span>
      <span class="badge__small badge__small--green">FRESH</span>
    </div>

    <footer class="pouch__bottom-band"></footer>
  </main>
</body>
</html>
```